Brighten Your Calling - book web site

I need a web site for my book that is being published and will be available on Tellurio April 6th. It will have an email opt in which will then email the person a pdf report.
And it will have a bio page.
My logo, pic, book cover and bio details are attached below.

Target Market(s)

New life coaches that are looking to figure out their purpose and branding for their business

Industry/Entity Type

Life Coaching

Number of Pages Required

3 page

Font styles to use
Serif

Requirements
Must have
• The book cover, my logo, an opt in page, a bio page, my picture
• i would like the book in the header
• Needs to be chatterloop compliant
Should not have
• except for the logo, willow heart and soul will NOT be highlighted in the header

```html
<!DOCTYPE html>
<html lang="en">
<head>
<meta charset="utf-8">
<title>Brighten Your Calling – a book by Marina Holloway</title>
<link rel="stylesheet" href="https://fonts.googleapis.com/css2?family=Sorts+Mill+Goudy&family=Roboto:wght@400;500&display=swap">
<style>
  :root {
    --ink: #1d1f20;
    --dark: #1c2326;
    --white: #ffffff;
    --brand: #d0281c;
    --muted: #3a3a3a;
    --grey-bg: #ececec;
    --floor: #f6f6f6;
    --contact-bg: #dcdcdc;
    --field-border: #3a4448;
    --field-text: #6b7478;
    --accent: #f5b50c;
    --ring: #f0b8b0;
    --photo-a: #8a8a8a;
    --photo-b: #5b4a42;
    --book-a: #5fa58c;
    --book-b: #3f7f6f;
  }
  * { margin: 0; padding: 0; box-sizing: border-box; }
  html, body { width: 1200px; height: 2394px; overflow: hidden; }
  body { position: relative; background: var(--white); font-family: "Roboto", Arial, sans-serif; color: var(--ink); }
  .serif { font-family: "Sorts Mill Goudy", Georgia, serif; }

  /* header */
  .site-header { position: absolute; left: 0; top: 0; width: 1200px; height: 64px; background: var(--white); z-index: 3; }
  .brand { position: absolute; left: 99px; top: 14px; display: flex; align-items: center; gap: 8px; }
  .brand-dot { width: 22px; height: 22px; border-radius: 50%; background: var(--accent); }
  .brand-name { font-family: "Sorts Mill Goudy", Georgia, serif; color: var(--brand); font-size: 20px; line-height: 1; letter-spacing: 0.5px; }
  .main-nav { position: absolute; right: 99px; top: 24px; display: flex; gap: 25px; }
  .main-nav a { font-family: "Sorts Mill Goudy", Georgia, serif; font-size: 13.5px; color: var(--ink); text-decoration: none; letter-spacing: 0.3px; }

  /* hero */
  .hero { position: absolute; left: 0; top: 64px; width: 1200px; height: 555px; background: var(--dark); }
  .hero-photo { position: absolute; left: 99px; top: 64px; width: 410px; height: 598px; background: linear-gradient(160deg, var(--photo-a), var(--photo-b)); box-shadow: 0 6px 14px rgba(0,0,0,0.35); z-index: 2; }
  .hero-title { position: absolute; left: 606px; top: 124px; color: var(--white); font-family: "Sorts Mill Goudy", Georgia, serif; font-weight: 400; white-space: nowrap; }
  .hero-title .big { display: block; font-size: 70px; line-height: 1; letter-spacing: 2px; }
  .hero-title .sub { display: block; font-size: 40px; line-height: 1.1; letter-spacing: 1px; margin-top: 4px; }
  .hero-text { position: absolute; left: 608px; top: 262px; width: 442px; color: var(--white); font-size: 17px; line-height: 25.5px; }

  /* book */
  .book { position: absolute; left: 0; top: 619px; width: 1200px; height: 650px; }
  .book-title { position: absolute; left: 99px; top: 138px; font-family: "Sorts Mill Goudy", Georgia, serif; font-weight: 400; font-size: 52px; line-height: 56px; color: var(--ink); letter-spacing: 1px; white-space: nowrap; }
  .book-copy { position: absolute; left: 99px; top: 280px; width: 500px; font-size: 15.5px; line-height: 21px; color: var(--muted); }
  .book-copy p + p { margin-top: 20px; }
  .buy-button { position: absolute; left: 99px; top: 508px; width: 129px; height: 51px; border: 2px solid #9a9a9a; border-radius: 8px; background: linear-gradient(#ffffff, #e4e4e4); box-shadow: 0 3px 4px rgba(0,0,0,0.25); text-align: center; text-decoration: none; color: var(--ink); }
  .buy-button .small { display: block; font-size: 8px; line-height: 10px; margin-top: 8px; letter-spacing: 0.3px; font-weight: 500; color: var(--ink); }
  .buy-button .store { display: block; font-size: 20px; line-height: 22px; color: var(--ink); }
  .book-cover { position: absolute; left: 766px; top: 123px; width: 291px; height: 479px; background: linear-gradient(170deg, var(--book-a), var(--book-b)); box-shadow: 6px 8px 12px rgba(0,0,0,0.25); }
  .deco { position: absolute; border-radius: 50%; border: 2px solid var(--ring); }

  /* video */
  .video { position: absolute; left: 0; top: 1269px; width: 1200px; height: 555px; background: var(--grey-bg); }
  .video-floor { position: absolute; left: 0; top: 410px; width: 1200px; height: 145px; background: var(--floor); }
  .video-title { position: absolute; left: 0; top: 38px; width: 1200px; text-align: center; font-family: "Sorts Mill Goudy", Georgia, serif; font-weight: 400; font-size: 54px; color: var(--ink); }
  .player { position: absolute; left: 247px; top: 131px; width: 728px; height: 338px; background: #000; border-radius: 3px; box-shadow: 0 8px 16px rgba(0,0,0,0.3); overflow: hidden; }
  .player-still { position: absolute; left: 203px; top: 0; width: 324px; height: 338px; background: linear-gradient(160deg, var(--photo-a), var(--photo-b)); }
  .player-caption { position: absolute; left: 11px; top: 8px; color: var(--white); font-size: 13.5px; }
  .player-icons { position: absolute; right: 10px; top: 8px; }
  .play { position: absolute; left: 340px; top: 152px; }

  /* contact */
  .contact-info { position: absolute; left: 0; top: 1824px; width: 600px; height: 506px; background: var(--contact-bg); }
  .contact-title { position: absolute; left: 99px; top: 50px; font-family: "Sorts Mill Goudy", Georgia, serif; font-weight: 400; font-size: 52px; color: #444; }
  .contact-row { position: absolute; left: 99px; display: flex; color: #333; }
  .contact-row .label { width: 94px; font-size: 20px; }
  .contact-row .value { font-size: 17px; line-height: 21px; padding-top: 2px; }
  .contact-form { position: absolute; left: 600px; top: 1824px; width: 600px; height: 506px; background: var(--dark); }
  .field { position: absolute; left: 70px; width: 355px; height: 39px; border: 1px solid var(--field-border); color: var(--field-text); font-size: 13px; padding: 10px 14px; }
  .field.message { height: 127px; }
  .send { position: absolute; left: 70px; top: 415px; width: 195px; height: 46px; background: var(--accent); color: var(--white); font-size: 18px; font-weight: 500; text-align: center; line-height: 46px; }

  /* footer */
  .site-footer { position: absolute; left: 0; top: 2330px; width: 1200px; height: 64px; background: var(--white); }
  .copyright { position: absolute; left: 99px; top: 25px; font-size: 12.5px; color: #333; }
  .footer-nav { position: absolute; right: 99px; top: 25px; display: flex; gap: 20px; }
  .footer-nav a { font-size: 12px; color: #333; text-decoration: none; }
</style>
</head>
<body>

<header class="site-header">
  <div class="brand"><span class="brand-dot"></span><span class="brand-name">WILLOW HEART AND SOUL</span></div>
  <nav class="main-nav">
    <a href="#">HOME</a><a href="#">ABOUT</a><a href="#">BOOKS</a><a href="#">BOOK CLUBS</a><a href="#">CONTACT</a>
  </nav>
</header>

<section class="hero">
  <h1 class="hero-title"><span class="big">BRIGHTEN</span><span class="sub">YOUR CALLING</span></h1>
  <p class="hero-text">Marina Holloway, author of Brighten Your Calling, helps new coaches and creative entrepreneurs find their inner voice so that they have the confidence to bring their authentic selves out into the world. Marina has gone through this process for herself and helped other new businesses achieve dramatic improvements in their organization and focus as a result.</p>
</section>
<div class="hero-photo" role="img" aria-label="Portrait photograph of the author"></div>

<section class="book">
  <span class="deco" style="left:4px;top:32px;width:30px;height:30px;border-color:#d0281c;"></span>
  <span class="deco" style="left:1150px;top:68px;width:24px;height:24px;"></span>
  <span class="deco" style="left:1070px;top:315px;width:20px;height:20px;"></span>
  <span class="deco" style="left:36px;top:450px;width:28px;height:28px;"></span>
  <span class="deco" style="left:744px;top:513px;width:20px;height:20px;"></span>
  <span class="deco" style="left:1170px;top:474px;width:22px;height:22px;"></span>
  <h2 class="book-title">THE BRIGHTEN<br>&nbsp;YOUR CALLING</h2>
  <div class="book-copy">
    <p>Marina Holloway, founder of Willow Heart and Soul, helps new coaches and creative entrepreneurs find their inner voice so that they have the confidence to bring their authentic selves out into the world.</p>
    <p>Marina’s keen sense of what works is backed by a thorough education in psychology, health, nutrition, training and management. She’s a certified health counselor, having trained at the Academy of Whole Wellness in New York (accredited by Harborview Teachers College).</p>
  </div>
  <a class="buy-button" href="#"><span class="small">BUY NOW FROM</span><span class="store serif">Tellurio</span></a>
  <div class="book-cover" role="img" aria-label="Book cover of Brighten Your Calling"></div>
</section>

<section class="video">
  <div class="video-floor"></div>
  <h2 class="video-title">Watch My Video</h2>
  <div class="player">
    <div class="player-still" role="img" aria-label="Video still of the author"></div>
    <span class="player-caption">Marina Holloway, founder of Willow Heart and Soul</span>
    <svg class="player-icons" width="30" height="14" viewBox="0 0 30 14">
      <circle cx="6" cy="7" r="5.5" fill="#fff"/><path d="M6 4v3.5l2 1.2" stroke="#000" stroke-width="1.3" fill="none"/>
      <path d="M19 10 Q20 5 25 5 V3 L29 6.5 L25 10 V8 Q21 8 19 10Z" fill="#fff"/>
    </svg>
    <svg class="play" width="48" height="34" viewBox="0 0 48 34">
      <rect width="48" height="34" rx="7" fill="#212121" fill-opacity="0.85"/>
      <path d="M19 11 L30 17 L19 23Z" fill="#fff"/>
    </svg>
  </div>
</section>

<section class="contact-info">
  <h2 class="contact-title">Get in Touch</h2>
  <div class="contact-row" style="top:148px;"><span class="label">Address:</span><span class="value">A-154 Lorem Vale Road<br>New York</span></div>
  <div class="contact-row" style="top:209px;"><span class="label">Emai :</span><span class="value">info@willowheart.com</span></div>
  <div class="contact-row" style="top:261px;"><span class="label">Phone:</span><span class="value">+91 900 555 0142</span></div>
</section>
<section class="contact-form">
  <div class="field" style="top:56px;">Name</div>
  <div class="field" style="top:126px;">Email</div>
  <div class="field" style="top:196px;">Phone</div>
  <div class="field message" style="top:268px;">Message</div>
  <div class="send">Send Message</div>
</section>

<footer class="site-footer">
  <span class="copyright">Copyright ©2017 Willow Heart and Soul - All Rights Reserved</span>
  <nav class="footer-nav"><a href="#">HOME</a><a href="#">ABOUT</a><a href="#">BOOKS</a><a href="#">BOOK CLUBS</a><a href="#">CONTACT</a></nav>
</footer>

</body>
</html>
```